Dane Moro films- wedding and event films company website. DESKTOP AND MOBILE

We need a website for a high-end wedding and event film production company. Looking for a very modern and elegant design. my old website is www.danemorofilms.example

I like the "white/black/rose gold" color scheme of my logo.

really looking for a sleek modern design the breaths professional and artistic.

Target Market(s)

wedding and event films.

Industry/Entity Type

Film Production

Number of Pages Required

5+ page

Colors

Designer to choose colors to be used in the design.

Requirements
Must have
• website name will be www.danemorofilms.example
• tagline is "CINEMATIC STORIES ABOUT YOU"
• sections: HOME, CONTACT, ABOUT, FILMS, BLOG
• You can see my old website at danemorofilms.example
• Website about section:
• Dane Moro Films was Established with the basis of truly cinematic and artistic films in mind. Dane and his team routinely travel the globe documenting weddings and events for high profile clients and discerning couples. Dane was born and raised in Maui Hawaii and has a unique approach to his films that embody the essence of a Hollywood film. Dane has spent the last 10 years traveling the world documenting corporate events and weddings with multiple Award winning production companies. In 2017 Dane decided to establish his own brand “Dane Moro films” that will take everything he has learned with his past experiences and push it to the next level. Aside from his personal achievements, Dane is extremely passionate about his craft and always looks forward to handcrafting beautiful wedding/event films for his clients. The style of work is non-traditional and the day of filming is extremely unobtrusive (as we are looking for natural-candid/ raw emotions).
• If you are looking for the best price in town, we are probably not the best option, but if you’re looking for the best quality and peace of mind on your wedding day, then you’re in the right place. Dane Moro Films is a boutique studio that only accepts a limited number of assignments per year. Inquire early to ensure availability.
• LINKS TO VIMEO VIDEOS THAT WILL BE IN THE "FILMS' SECTION.
• BRENT FILM TRAILER - https://clipvault.example/418205736
• BRENT FEATURE FILM - https://clipvault.example/527910384
• NORA AND PAUL'S WEDDING - https://clipvault.example/649382015
• DRONE DEMO REEL - https://clipvault.example/751046923
• WEDDING INDUSTRY EVENT PARTY - https://clipvault.example/862937104/7a2d9c3e8b
• images that you can use on site are here: https://maribelortegaphotos.picvault.example/gallery/ruth&glen/
• password is: meadow

```html
<!DOCTYPE html>
<html lang="en">
<head>
<meta charset="utf-8">
<title>Dane Moro Films — Cinematic Stories About You</title>
<link href="https://fonts.googleapis.com/css2?family=Lato:wght@300;400;700;900&display=swap" rel="stylesheet">
<style>
:root{
  --rose:#d08a55;
  --rose-dark:#b5703d;
  --rose-light:#e4a675;
  --ink:#1b1b1b;
  --text:#444;
  --muted:#8a8a8a;
  --line:#dcdcdc;
  --paper:#ffffff;
  --mist:#efede9;
  --night:#141414;
}
*{box-sizing:border-box;margin:0;padding:0}
html,body{width:1200px;height:3846px;overflow:hidden}
body{position:relative;font-family:"Lato",sans-serif;color:var(--text);background:var(--paper)}
.abs{position:absolute}
.btn{position:absolute;display:flex;align-items:center;justify-content:center;background:linear-gradient(var(--rose-light),var(--rose-dark));color:#fff;font-size:12px;font-weight:700;letter-spacing:.5px;text-transform:uppercase;border-radius:2px}

/* header */
.site-header{position:absolute;left:0;top:0;width:1200px;height:120px;background:#fff;box-shadow:0 1px 4px rgba(0,0,0,.08);z-index:2}
.brand{position:absolute;left:141px;top:44px;display:flex;align-items:center;gap:12px;font-size:24px;font-weight:700;letter-spacing:1.5px;color:#5a5a5a}
.brand-mark{width:18px;height:18px;background:var(--rose)}
.main-nav{position:absolute;left:540px;top:72px;display:flex;font-size:13px;font-weight:700;color:#333;text-transform:uppercase}
.main-nav a{padding:0 30px;border-left:1px solid #ccc;line-height:20px;color:inherit;text-decoration:none}
.main-nav a:first-child{border-left:none;color:var(--rose)}

/* hero */
.hero{position:absolute;left:0;top:120px;width:1200px;height:521px;background:linear-gradient(100deg,#6d7075 0%,#9aa0a6 30%,#cfd3d6 55%,#6a6b63 80%,#4d4a42 100%)}
.hero-frame{position:absolute;left:133px;top:175px;width:434px;height:264px;border:2px solid rgba(255,255,255,.85);text-align:center;color:#fff}
.hero-title{position:absolute;left:0;right:0;top:82px;font-size:33px;font-weight:700;line-height:43px;text-transform:uppercase;text-shadow:0 1px 3px rgba(0,0,0,.4)}

/* divider */
.divider{position:absolute;height:12px}
.divider::before{content:"";position:absolute;left:0;right:0;top:6px;border-top:1px solid var(--line)}
.divider i{position:absolute;left:0;top:1px;width:10px;height:10px;border-radius:50%;background:#c8c8c8}
.divider.center i{left:50%;margin-left:-5px}

/* about */
.about-photo{position:absolute;left:133px;top:713px;width:452px;height:490px;border:1px solid #ddd;padding:9px;background:#fff}
.about-photo div{width:100%;height:100%;background:linear-gradient(160deg,#d9d9d9,#7d7d7d 60%,#3a3a3a)}
.section-title{position:absolute;font-size:28px;font-weight:900;color:var(--ink);text-transform:uppercase}
.section-title span{color:var(--rose)}
.about-copy{position:absolute;left:623px;width:444px;font-size:13.5px;line-height:21px;text-align:justify;color:#333}
.about-sub{position:absolute;left:623px;top:1034px;font-size:16px;font-weight:700;color:var(--rose)}

/* quote */
.quote-band{position:absolute;left:0;top:1264px;width:1200px;height:244px;background:linear-gradient(var(--rose-light),var(--rose-dark));color:#fff;text-align:center}
.quote-band p{position:absolute;left:0;right:0;top:60px;font-size:28px;font-weight:300;line-height:46px}
.quote-band cite{position:absolute;left:0;right:0;top:152px;font-style:normal;font-size:26px;font-weight:700}

/* films */
.films{position:absolute;left:0;top:1508px;width:1200px;height:564px;background:var(--mist)}
.video{position:absolute;top:176px;width:447px;height:249px;overflow:hidden}
.video .bar{position:absolute;left:0;right:0;bottom:0;height:24px;background:rgba(20,20,20,.75)}
.video .bar i{position:absolute;left:64px;right:60px;top:10px;height:5px;background:#7bb7e0}
.video .bar b{position:absolute;left:14px;top:6px;width:0;height:0;border-left:10px solid #fff;border-top:6px solid transparent;border-bottom:6px solid transparent}
.video .tools{position:absolute;right:8px;top:10px;width:26px}
.video .tools span{display:block;width:26px;height:20px;margin-bottom:6px;background:rgba(20,20,20,.75);border-radius:3px}
.dots{position:absolute;left:577px;top:494px;display:flex;gap:5px}
.dots span{width:8px;height:6px;border-radius:3px;background:#e7b99a}
.dots span.on{width:18px;background:var(--rose)}

/* cta */
.cta{position:absolute;left:0;top:2133px;width:1200px;height:359px}
.cta-copy{position:absolute;left:0;top:0;width:600px;height:359px;background:var(--night)}
.cta-copy h2{position:absolute;left:133px;top:80px;width:460px;font-size:24px;font-weight:700;line-height:36px;color:#fff}
.cta-photo{position:absolute;left:600px;top:0;width:600px;height:359px;background:linear-gradient(180deg,#e9e6df 0%,#c9b79a 35%,#7b5e3e 65%,#2d3a4a 100%)}

/* blog */
.post{position:absolute;top:2666px;width:295px;height:364px;background:#fff;box-shadow:0 1px 6px rgba(0,0,0,.15)}
.post .thumb{height:185px}
.post h3{position:absolute;left:16px;top:202px;font-size:14px;font-weight:700;color:#222}
.post .meta{position:absolute;left:16px;top:228px;font-size:11px;color:var(--muted)}
.post p{position:absolute;left:16px;right:14px;top:248px;font-size:13px;line-height:21px;color:#333}
.arrow{position:absolute;top:2830px;width:14px;height:14px;border-left:2px solid #bbb;border-bottom:2px solid #bbb}

/* contact */
.contact{position:absolute;left:0;top:3110px;width:1200px;height:664px;background:radial-gradient(circle at 85% 70%,#5a4a38 0%,#2a2520 40%,#1a1a1a 80%)}
.contact .section-title{color:#fff}
.contact-panel{position:absolute;left:236px;top:205px;width:728px;height:403px;background:rgba(190,130,85,.72);color:#fff;text-align:center}
.send-badge{position:absolute;left:338px;top:-26px;width:52px;height:52px;border-radius:50%;background:#fff;display:flex;align-items:center;justify-content:center}
.contact-info{position:absolute;left:0;right:0;top:62px;font-size:14px;line-height:26px}
.field{position:absolute;background:#f2ede8;font-size:11px;color:#555;padding:8px 12px;text-align:left}
.btn-ghost{position:absolute;left:302px;top:323px;width:121px;height:39px;border:1px solid #fff;color:#fff;font-size:12px;font-weight:700;display:flex;align-items:center;justify-content:center}
.site-footer{position:absolute;left:0;top:3774px;width:1200px;height:72px;background:#111;color:#ddd;font-size:12px;text-align:center;line-height:72px}
</style>
</head>
<body>

<header class="site-header">
  <div class="brand"><span class="brand-mark"></span>DANE MORO FILMS</div>
  <nav class="main-nav"><a href="#">Home</a><a href="#">About</a><a href="#">Films</a><a href="#">Blog</a><a href="#">Contact</a></nav>
</header>

<section class="hero" role="img" aria-label="Bride and groom embracing on a rocky seaside cliff with a lighthouse at sunset">
  <div class="hero-frame">
    <h1 class="hero-title">Cinematic<br>Stories About You</h1>
    <div class="btn" style="left:45px;top:177px;width:317px;height:36px">Book your wedding or event now !</div>
  </div>
</section>

<section class="about">
  <div class="about-photo"><div role="img" aria-label="Black and white portrait of the filmmaker"></div></div>
  <h2 class="section-title" style="left:623px;top:704px">About <span>Us</span></h2>
  <div class="divider" style="left:623px;width:444px;top:769px"><i></i></div>
  <p class="about-copy" style="top:815px">At Dane Moro Films we specialize in offering the finest in wedding and corporate cinematography. We offer a very modern and creative style for capturing your special moments with a beautiful and cinematic approach that enables us to produce the highest quality of films. Dane and his hand selected team have over 10 years of experience, and they strive to make the best films in the industry. We pride ourselves on remaining attentive to clients' needs, business practices rooted in integrity, and continually striving to be at the forefront of innovation in our industry.</p>
  <h3 class="about-sub">The Cinematic Difference</h3>
  <p class="about-copy" style="top:1067px">We pride ourselves on using the best quality cinema tools for our films. The equipment we use are industry standard cinematic tools used in hollywood movies, using such tools gives our films a truely cinematic feel.</p>
  <div class="btn" style="left:623px;top:1164px;width:120px;height:37px">Read More</div>
</section>

<section class="quote-band">
  <p>“Dane really is one of the best film makers in Hawaii, great<br>work Dane! We loved the film!”</p>
  <cite>— Leia Kanoa</cite>
</section>

<section class="films">
  <h2 class="section-title" style="left:0;right:0;top:56px;text-align:center;font-size:26px">Films</h2>
  <div class="divider center" style="left:133px;width:934px;top:119px"><i></i></div>
  <div class="video" style="left:133px;background:linear-gradient(180deg,#3a2a2a,#8a5a7a 45%,#2a3a5a)" role="img" aria-label="Wedding film still of a chandelier-lit reception hall">
    <div class="tools"><span></span><span></span><span></span><span></span></div>
    <div class="bar"><b></b><i></i></div>
  </div>
  <div class="video" style="left:620px;background:linear-gradient(180deg,#c9d4dc,#9aa58a 50%,#d8d4cc)" role="img" aria-label="Wedding film still of an outdoor garden ceremony">
    <div class="tools"><span></span><span></span><span></span><span></span></div>
    <div class="bar"><b></b><i></i></div>
  </div>
  <div class="dots"><span></span><span class="on"></span><span></span></div>
</section>

<section class="cta">
  <div class="cta-copy">
    <h2>You’re Looking For The Best Quality And Peace Of Mind On Your Wedding Day, Then You’re In The Right Place</h2>
    <div class="btn" style="left:133px;top:225px;width:318px;height:36px">Book your wedding or event now !</div>
  </div>
  <div class="cta-photo" role="img" aria-label="Evening wedding reception on a terrace beside a lit swimming pool"></div>
</section>

<section class="blog">
  <h2 class="section-title" style="left:0;right:0;top:2547px;text-align:center;font-size:27px">Latest <span>Blog</span></h2>
  <div class="divider center" style="left:133px;width:934px;top:2614px"><i></i></div>
  <div class="arrow" style="left:100px;transform:rotate(45deg)"></div>
  <div class="arrow" style="left:1086px;transform:rotate(-135deg)"></div>
  <article class="post" style="left:133px">
    <div class="thumb" role="img" aria-label="Elegant reception table setting" style="background:linear-gradient(#5a3a30,#c9b5a5)"></div>
    <h3>Uis nostrud exercitation an ullamco</h3>
    <div class="meta">By Dane &nbsp;|&nbsp; Nov 02, 2017</div>
    <p>Ut enim ad minim veniam, quis nostrud exercitation an ullamco laboris nisi ut</p>
    <div class="btn" style="left:16px;top:303px;width:118px;height:36px">Read More</div>
  </article>
  <article class="post" style="left:453px">
    <div class="thumb" role="img" aria-label="Couple walking hand in hand outside a venue" style="background:linear-gradient(#8b9aa8,#3c4452 60%,#a89a88)"></div>
    <h3>Uis nostrud exercitation an ullamco</h3>
    <div class="meta">By Dane &nbsp;|&nbsp; Nov 02, 2017</div>
    <p>Ut enim ad minim veniam, quis nostrud exercitation an ullamco laboris nisi ut</p>
    <div class="btn" style="left:16px;top:303px;width:118px;height:36px">Read More</div>
  </article>
  <article class="post" style="left:772px">
    <div class="thumb" role="img" aria-label="Garden path with cypress trees leading to a villa" style="background:linear-gradient(#bcd0e2,#6f8a4f 55%,#c9b89a)"></div>
    <h3>Uis nostrud exercitation an ullamco</h3>
    <div class="meta">By Dane &nbsp;|&nbsp; Nov 02, 2017</div>
    <p>Ut enim ad minim veniam, quis nostrud exercitation an ullamco laboris nisi ut</p>
    <div class="btn" style="left:16px;top:303px;width:118px;height:36px">Read More</div>
  </article>
</section>

<section class="contact" role="img" aria-label="Dim candlelit evening backdrop with a lantern">
  <h2 class="section-title" style="left:0;right:0;top:60px;text-align:center;font-size:27px">Contact Us</h2>
  <div class="divider center" style="left:133px;width:934px;top:125px"><i style="background:#888"></i></div>
  <div class="contact-panel">
    <div class="send-badge">
      <svg width="24" height="24" viewBox="0 0 24 24"><path d="M2 11 22 3 15 21 11 13Z M11 13 22 3" fill="none" stroke="#333" stroke-width="1.8" stroke-linejoin="round"/></svg>
    </div>
    <div class="contact-info">Email: dane@danemorofilms.example<br>Phone: (808) 555-0147</div>
    <div class="field" style="left:41px;top:128px;width:318px;height:39px">Name*</div>
    <div class="field" style="left:369px;top:128px;width:318px;height:39px">Email*</div>
    <div class="field" style="left:41px;top:177px;width:646px;height:136px">Message*</div>
    <div class="btn-ghost">READ MORE</div>
  </div>
</section>

<footer class="site-footer">Copyright © 2017 Dane Moro Films. All Rights Reserved</footer>

</body>
</html>
```